Design needed for Cover of Conference Brochure

We are a conference company that puts on several business conferences per year. We are putting together a new conference - the Brightpath Insight Forum, and our audience is UX practitioners and specialists, product designers, UX designers, etc.
We need a brochure cover created. We are looking for fresh design ideas and are open to varying color schemes - please just keep in mind that this is a conference for business professionals, and fonts and colors should reflect this. Only restriction is that we do have a general cover format that we follow - i.e. which text goes where. (I've attached samples from our other events to reference.) We also generally have a central image to each brochure - feel free to submit a few versions with different images... we want something that accurately represents UX. However, if the design is compelling enough, image might not be completely necessary. We are relatively flexible - we just want something sharp!
- Must include KLVO logo (see placing on sample event covers)
- Must include footer - see sample covers
- Red text in word document are notes to you the designer - not actual text meant to appear on the cover
This cover is standard 8x11, and will be used for web only, not print. I have attached a word doc that includes all of the text that you will need for the cover. We will need final version in PDF, jpeg, and PSD. Please message me with any questions or clarification.

```html
<!DOCTYPE html>
<html lang="en">
<head>
<meta charset="utf-8">
<title>Brightpath Insight Forum</title>
<link rel="stylesheet" href="https://fonts.googleapis.com/css2?family=Arimo&family=Jost:wght@400;500;600;700&family=Open+Sans:ital,wght@0,400;0,700;1,400&family=Tinos:wght@400;700&display=swap">
<style>
  :root {
    --stage: #eafbf8;
    --page: #ffffff;
    --ink: #1a1a1a;
    --band: #1b1b1b;
    --cyan: #19e9f2;
    --cyan-soft: #6ff4f6;
    --hero-a: #c6f5f7;
    --hero-b: #e8fefe;
    --badge: #dcdcdc;
    --badge-ink: #2a2a2a;
  }
  * { box-sizing: border-box; margin: 0; padding: 0; }
  html, body { width: 1200px; height: 1000px; overflow: hidden; background: var(--stage); }
  .page {
    position: absolute; left: 257px; top: 90px; width: 668px; height: 826px;
    background: var(--page); box-shadow: 10px 12px 16px rgba(0,60,60,.18);
    font-family: "Open Sans", sans-serif; color: var(--ink);
  }
  .site-title {
    position: absolute; left: 17px; top: 32px; white-space: nowrap;
    font-family: "Arimo", sans-serif; font-weight: 400; font-size: 30px; color: var(--cyan); letter-spacing: .2px;
  }
  .tagline {
    position: absolute; left: 18px; top: 75px;
    font-family: "Jost", sans-serif; font-weight: 600; font-size: 12px;
  }
  .nav {
    position: absolute; left: 0; top: 109px; width: 668px; height: 33px; background: var(--band);
    display: flex; justify-content: flex-end; align-items: center; gap: 23px; padding-right: 16px;
  }
  .nav span { font-family: "Jost", sans-serif; font-weight: 600; font-size: 13.5px; color: #fff; letter-spacing: .3px; }
  .hero {
    position: absolute; left: 0; top: 142px; width: 668px; height: 215px;
    background: linear-gradient(180deg, var(--hero-a), var(--hero-b));
  }
  .badge {
    position: absolute; left: 8px; top: 20px; width: 178px; height: 178px; border-radius: 50%;
    background: var(--badge); box-shadow: 6px 8px 10px rgba(0,0,0,.25);
    display: flex; align-items: center; justify-content: center; text-align: center;
    font-family: "Jost", sans-serif; font-weight: 600; font-size: 17px; line-height: 20px; color: var(--badge-ink);
  }
  .hero-visual {
    position: absolute; left: 213px; top: 14px; width: 445px; height: 196px; border-radius: 8px;
    background: linear-gradient(90deg, #e82a2a, #f0c020 25%, #3fe04a 45%, #1ad6e8 62%, #3a5de8 80%, #8a2fc8);
    opacity: .85;
  }
  .news {
    position: absolute; left: 10px; top: 380px; width: 216px; height: 287px; border-radius: 14px;
    background: var(--band); color: #fff;
  }
  .search-field {
    position: absolute; left: 29px; top: 8px; width: 146px; height: 29px; border-radius: 15px;
    background: #fff; color: var(--ink); font-size: 11px; display: flex; align-items: center; justify-content: center;
  }
  .search-btn {
    position: absolute; left: 53px; top: 47px; width: 89px; height: 23px; border-radius: 3px;
    background: var(--cyan); color: #fff; font-family: "Jost", sans-serif; font-weight: 600; font-size: 13px;
    display: flex; align-items: center; justify-content: center; letter-spacing: .5px;
  }
  .news h2 {
    position: absolute; left: 0; width: 100%; top: 86px; text-align: center;
    font-family: "Jost", sans-serif; font-weight: 400; font-size: 25px;
  }
  .news p {
    position: absolute; left: 20px; width: 185px; font-family: "Tinos", serif; font-size: 12.5px; line-height: 16.5px;
  }
  .news .lead { top: 122px; }
  .news .details { top: 202px; font-weight: 700; }
  .welcome {
    position: absolute; left: 254px; top: 384px; white-space: nowrap;
    font-family: "Jost", sans-serif; font-weight: 700; font-size: 16.5px; letter-spacing: .2px;
  }
  .highlights-title {
    position: absolute; left: 255px; top: 424px; white-space: nowrap;
    font-style: italic; font-size: 16.5px; text-decoration: underline; text-underline-offset: 4px;
  }
  .highlights { position: absolute; left: 280px; top: 470px; list-style: none; }
  .highlights li { display: flex; align-items: center; gap: 12px; height: 42px; margin-bottom: 26px; font-size: 15.5px; line-height: 21px; }
  .highlights li.tall { height: 63px; }
  .highlights svg { flex: 0 0 44px; }
  .highlights b { font-weight: 700; }
  .footer {
    position: absolute; left: 0; top: 756px; width: 668px; height: 70px; background: var(--band);
  }
  .footer .register {
    position: absolute; left: 46px; top: 13px; color: #fff; font-size: 17px; white-space: nowrap;
  }
  .footer .register strong { font-family: "Jost", sans-serif; font-weight: 600; margin-right: 14px; }
  .footer .register .at { margin-right: 18px; }
  .footer .contact { position: absolute; left: 44px; top: 40px; color: var(--cyan-soft); font-size: 17px; white-space: nowrap; }
  .brand {
    position: absolute; right: 12px; top: 16px; display: flex; align-items: center; gap: 6px;
    font-family: "Open Sans", sans-serif; font-weight: 700; font-size: 15px; color: #fff;
  }
  .brand i { width: 14px; height: 14px; background: var(--cyan); display: block; }
</style>
</head>
<body>
  <main class="page">
    <h1 class="site-title">BRIGHTPATH INSIGHT FORUM</h1>
    <p class="tagline">Design Compelling Experiences through Successful UX Strategy</p>

    <nav class="nav">
      <span>HOME</span><span>ABOUT</span><span>SUMMIT</span><span>HIGHLIGHTS</span><span>CONTACT</span>
    </nav>

    <section class="hero">
      <div class="badge">Register by<br>March 7th, 2014<br>&amp;<br>SAVE $400 !</div>
      <div class="hero-visual" role="img" aria-label="Phone, laptop and tablet showing a rainbow word cloud of UX terms such as strategy, research and design"></div>
    </section>

    <aside class="news">
      <div class="search-field">Brightpath Insight Forum</div>
      <div class="search-btn">SEARCH</div>
      <h2>NEWS</h2>
      <p class="lead">Brightpath Insight Forum 2014 Conference to be held in San Fransisco, mark your calendar right now...</p>
      <p class="details">Dates : June 10-12, 2014<br>Venue :<br>Harborline Conference Hall, San Francisco, CA</p>
    </aside>

    <h2 class="welcome">WELCOME TO BRIGHTPATH INSIGHT FORUM</h2>
    <p class="highlights-title">HIGHLIGHTS OF BRIGHTPATH INSIGHT FORUM</p>

    <ul class="highlights">
      <li><svg width="44" height="42" viewBox="0 0 44 42"><path d="M0 12h24V0l20 21-20 21V30H0z" fill="#19e9f2"/></svg><span>Case Studies from Leading Brands on<br>Executing an Effective UX Strategy</span></li>
      <li><svg width="44" height="42" viewBox="0 0 44 42"><path d="M0 12h24V0l20 21-20 21V30H0z" fill="#19e9f2"/></svg><span>Learn How UX-Driven Innovation Can<br>Change Your Business</span></li>
      <li><svg width="44" height="42" viewBox="0 0 44 42"><path d="M0 12h24V0l20 21-20 21V30H0z" fill="#19e9f2"/></svg><span>Build a Successful UX Team that<br>Operates Strategically</span></li>
      <li class="tall"><svg width="44" height="42" viewBox="0 0 44 42"><path d="M0 12h24V0l20 21-20 21V30H0z" fill="#19e9f2"/></svg><span>Insights into UX Research, User<br>Behavior, Usability Testing, Lean UX,<br>and <b>More....</b></span></li>
    </ul>

    <footer class="footer">
      <p class="register"><strong>Register Today</strong><span class="at">@</span>http://www.brightpathinsightforum.com</p>
      <p class="contact">For More Details, Contact us at 888.555.0142</p>
      <div class="brand"><i></i>KLVO</div>
    </footer>
  </main>
</body>
</html>
```